Brookvale Advisors LLC web site

Brookvale Advisors LLC is a consulting and recruiting firm that provides education, perspective, guidance, and assistance to financial advisors. Dennis Halloway is the founder of this new firm and is the only employee at this time.
Please see the attached overview which will provide much narrative describing the firm, its purpose, scope of services offered, and other useful information to help you design a web site.

Target Market(s)

US based financial advisors who are looking to transition their business to an independent ( non-employee ) business model.

Industry/Entity Type

Consultant

Coding

Coded - Design and coding required

Number of Pages Required

5+ page

Font styles to use
Sans Serif

Requirements
Must have
• all relevant pages for a basic web site : Home, About, Services offered, Contact, Resources , etc.
Nice to have
• color scheme : see logo in the attached briefing document

```html
<!DOCTYPE html>
<html lang="en">
<head>
<meta charset="utf-8">
<title>Brookvale Advisors LLC</title>
<link rel="stylesheet" href="https://fonts.googleapis.com/css2?family=Libre+Baskerville&family=Roboto:wght@400;500;700&display=swap">
<style>
:root{
  --navy:#0b4a7d;
  --navy-dark:#083a63;
  --ink:#1d1d1d;
  --muted:#7a7a7a;
  --light:#f2f3f5;
  --footer:#5b5b5b;
  --white:#ffffff;
  --serif:'Libre Baskerville',Georgia,serif;
  --sans:'Roboto',Arial,sans-serif;
}
*{box-sizing:border-box;margin:0;padding:0}
html,body{width:1200px;height:4070px;overflow:hidden}
body{font-family:var(--sans);color:var(--ink);background:var(--white);position:relative}
section,header,footer{position:absolute;left:0;width:1200px}
.abs{position:absolute}
.heading{font-family:var(--serif);text-transform:uppercase;color:var(--navy);font-weight:400;letter-spacing:1px}
.btn{position:absolute;display:flex;align-items:center;justify-content:center;gap:10px;border-radius:30px;font:700 13px var(--sans);text-transform:uppercase;color:var(--white);background:var(--navy)}
.btn .dot{width:13px;height:13px;border-radius:50%;background:var(--white);display:inline-flex;align-items:center;justify-content:center}
.btn .dot::after{content:"";border-left:5px solid var(--navy);border-top:3.5px solid transparent;border-bottom:3.5px solid transparent;margin-left:2px}
.btn.ring{box-shadow:0 0 0 3px var(--white),0 0 0 5px var(--navy)}
.btn.grey{background:#4b4b4b;box-shadow:0 0 0 3px #f2f3f5,0 0 0 5px #4b4b4b}
.btn.grey .dot::after{border-left-color:#4b4b4b}

/* header */
.site-header{top:0;height:85px;background:var(--white)}
.brand{left:110px;top:22px;display:flex;align-items:center;gap:10px}
.brand-mark{width:40px;height:40px;border-radius:50%;background:var(--navy)}
.brand-name{font:700 17px/1.15 var(--sans);color:var(--navy);letter-spacing:1.5px;text-transform:uppercase}
.main-nav{left:445px;top:32px;display:flex;gap:29px;font:700 13px var(--sans);text-transform:uppercase}
.main-nav .active{color:var(--navy)}
.login{left:968px;top:20px;width:118px;height:42px;border-radius:12px;box-shadow:0 0 0 3px var(--white),0 0 0 5px var(--navy)}
.lock{width:9px;height:8px;background:var(--white);border-radius:1px;position:relative;margin-top:4px}
.lock::before{content:"";position:absolute;left:1px;top:-6px;width:5px;height:6px;border:1.5px solid var(--white);border-bottom:none;border-radius:4px 4px 0 0}

/* hero */
.hero{top:85px;height:558px;background:linear-gradient(180deg,#f6f6f6 0%,#f2f2f2 45%,#bdbdbd 100%)}
.hero-photo{left:0;bottom:0;width:1200px;height:330px;background:linear-gradient(90deg,rgba(120,120,120,.55),rgba(235,235,235,.1) 30%,rgba(235,235,235,.1) 55%,rgba(110,110,110,.55))}
.hero h1{position:absolute;top:120px;width:100%;text-align:center;font:400 33px/42px var(--serif);letter-spacing:1.5px;color:#111;text-transform:uppercase}
.hero p{position:absolute;top:228px;left:240px;width:720px;text-align:center;font:400 14px/26px var(--sans);color:#444}
.hero .btn{left:533px;top:298px;width:160px;height:44px}
.arrow{position:absolute;top:262px}

/* provide */
.provide{top:643px;height:557px}
.provide .heading{position:absolute;top:92px;width:100%;text-align:center;font-size:29px}
.service{position:absolute;top:175px;width:230px;text-align:center}
.blob{width:180px;height:160px;margin:0 auto;position:relative}
.service h3{margin-top:36px;font:500 15px var(--sans);text-transform:uppercase;letter-spacing:.3px}
.service h3::after{content:"";display:block;width:30px;height:3px;background:var(--navy);margin:12px auto 0}
.service p{margin-top:14px;font:400 13px/20px var(--sans);color:var(--muted)}

/* about */
.about{top:1200px;height:466px;background:var(--navy);overflow:hidden}
.about-photo{left:-610px;top:-362px;width:1190px;height:1190px;border-radius:50%;border:6px solid #5d5d5d;background:radial-gradient(circle at 78% 50%,#3d6d87 0%,#7ea6b6 30%,#c9d4d9 55%,#e3dfdc 75%)}
.about .heading{position:absolute;left:665px;top:58px;color:var(--white);font-size:30px}
.about p{position:absolute;left:665px;top:122px;width:428px;font:400 13.5px/26px var(--sans);color:var(--white)}
.about .btn{left:667px;top:352px;width:156px;height:44px;background:#575757;box-shadow:0 0 0 3px var(--navy),0 0 0 5px #bfbfbf}
.about .btn .dot::after{border-left-color:#575757}

/* why */
.why{top:1666px;height:537px}
.why .heading{position:absolute;top:96px;width:100%;text-align:center;font-size:30px}
.reason{position:absolute;top:174px;width:236px;height:252px;border-radius:12px;overflow:hidden}
.reason span{position:absolute;bottom:34px;width:100%;text-align:center;font:700 13px var(--sans);color:var(--white);text-transform:uppercase}

/* founder */
.founder{top:2203px;height:516px;background:var(--light)}
.founder .heading{position:absolute;left:110px;top:88px;font-size:30px}
.founder p{position:absolute;left:108px;top:145px;width:420px;font:400 13.5px/26px var(--sans);color:#666}
.contact-row{position:absolute;display:flex;align-items:center;gap:14px;font:400 14px var(--sans)}
.ico{width:34px;height:34px;border-radius:50%;background:var(--navy);display:flex;align-items:center;justify-content:center;flex:none}
.founder .btn{left:110px;top:2358px;}
.frame{left:641px;top:70px;width:388px;height:363px;background:var(--navy)}
.portrait{left:652px;top:80px;width:378px;height:355px;background:linear-gradient(160deg,#3a3a3a,#545454 50%,#2f3640)}

/* resources */
.resources{top:2719px;height:676px}
.resources .heading{position:absolute;top:96px;width:100%;text-align:center;font-size:30px}
.post{position:absolute;top:164px;width:320px;height:420px;background:var(--white);box-shadow:0 0 6px rgba(0,0,0,.15)}
.post .pic{position:absolute;left:6px;top:6px;width:308px;height:212px}
.post h4{position:absolute;left:22px;top:243px;width:280px;font:700 13px/22px var(--sans);text-transform:uppercase}
.post p{position:absolute;left:22px;top:302px;width:280px;font:400 13.5px/23px var(--sans);color:#666}
.post .more{position:absolute;left:22px;top:361px;font:700 11px var(--sans);color:var(--navy);text-decoration:underline;text-transform:uppercase}
.post .meta{position:absolute;left:0;bottom:0;width:100%;height:40px;border-top:1px solid #e4e4e4;display:flex;align-items:center;gap:30px;padding-left:22px;font:400 13px var(--sans);color:#666}
.meta span{display:flex;align-items:center;gap:10px}
.round-arrow{position:absolute;top:359px;width:42px;height:42px;border-radius:50%;background:var(--white);box-shadow:0 0 5px rgba(0,0,0,.2);display:flex;align-items:center;justify-content:center}

/* touch */
.touch{top:3395px;height:437px;background:linear-gradient(180deg,#2f6c99 0%,#3a77a3 50%,#2a6494 100%)}
.touch .heading{position:absolute;top:60px;color:var(--white);font-size:27px}
.field{position:absolute;background:var(--white);border-radius:3px;font:400 13px var(--sans);color:#666;padding:14px 10px}
.submit{left:115px;top:338px;width:150px;height:50px;border-radius:3px;background:var(--navy);box-shadow:0 0 0 2px var(--white)}
.citem{position:absolute;left:782px;display:flex;align-items:center;gap:26px;font:700 15px/20px var(--sans);color:var(--white)}
.citem .ico{width:44px;height:44px;background:var(--white)}

/* footer */
.site-footer{top:3832px;height:238px;background:var(--footer);color:var(--white)}
.foot-nav{position:absolute;top:72px;width:100%;display:flex;justify-content:center;gap:29px;font:500 13px var(--sans);text-transform:uppercase}
.social{position:absolute;top:112px;width:100%;display:flex;justify-content:center;gap:8px}
.social i{width:22px;height:22px;border-radius:50%;background:#2f7fd0;display:block}
.copy{position:absolute;top:158px;width:100%;text-align:center;font:400 13px var(--sans)}
</style>
</head>
<body>

<header class="site-header">
  <div class="abs brand"><span class="brand-mark"></span><span class="brand-name">Brookvale<br>Advisors LLC</span></div>
  <nav class="abs main-nav"><span class="active">Home</span><span>About</span><span>Services Offered</span><span>Contact</span><span>Resources</span></nav>
  <div class="btn login">Log In <span class="lock"></span></div>
</header>

<section class="hero">
  <div class="abs hero-photo" role="img" aria-label="Upward view of glass office towers in greyscale"></div>
  <h1>Helping financial advisors to navigate<br>their journey to independence</h1>
  <p>Brookvale Advisors LLC is a consulting and recruiting firm that provides education, perspective, guidance, and assistance to financial advisors</p>
  <div class="btn ring">Get Started <span class="dot"></span></div>
  <svg class="arrow" style="left:52px" width="22" height="30" viewBox="0 0 22 30"><path d="M16 3 5 15l11 12" fill="none" stroke="#111" stroke-width="3"/></svg>
  <svg class="arrow" style="left:1126px" width="22" height="30" viewBox="0 0 22 30"><path d="M6 3l11 12L6 27" fill="none" stroke="#111" stroke-width="3"/></svg>
</section>

<section class="provide">
  <h2 class="heading">What we provide</h2>
  <div class="service" style="left:107px">
    <svg class="blob" viewBox="0 0 180 160"><path d="M20 14h140c12 0 18 12 12 26-18 44-48 90-74 112-6 5-12 5-18 0C54 130 24 86 8 40 3 26 8 14 20 14z" fill="#0b4a7d" stroke="#fff" stroke-width="5"/><path d="M14 8h152c14 0 22 16 16 32" fill="none" stroke="#ddd" stroke-width="2"/><rect x="76" y="42" width="44" height="32" rx="2" fill="none" stroke="#fff" stroke-width="4"/><circle cx="66" cy="62" r="7" fill="#fff"/><path d="M56 110V78h18l10 10" fill="none" stroke="#fff" stroke-width="6"/><path d="M96 74l-8 36M104 74l8 36" stroke="#fff" stroke-width="4"/></svg>
    <h3>Education</h3><p>Lorem ipsum dolor sit consectetur adipiscing elit, sed do eiusmod</p>
  </div>
  <div class="service" style="left:359px">
    <svg class="blob" viewBox="0 0 180 160"><path d="M20 14h140c12 0 18 12 12 26-18 44-48 90-74 112-6 5-12 5-18 0C54 130 24 86 8 40 3 26 8 14 20 14z" fill="#0b4a7d" stroke="#fff" stroke-width="5"/><path d="M90 36l30 17v34l-30 17-30-17V53z" fill="none" stroke="#fff" stroke-width="5"/><path d="M60 53l30 17 30-17M90 70v34" fill="none" stroke="#fff" stroke-width="5"/></svg>
    <h3>Perspective</h3><p>Lorem ipsum dolor sit consectetur adipiscing elit, sed do eiusmod</p>
  </div>
  <div class="service" style="left:611px">
    <svg class="blob" viewBox="0 0 180 160"><path d="M20 14h140c12 0 18 12 12 26-18 44-48 90-74 112-6 5-12 5-18 0C54 130 24 86 8 40 3 26 8 14 20 14z" fill="#0b4a7d" stroke="#fff" stroke-width="5"/><rect x="80" y="42" width="38" height="56" fill="none" stroke="#fff" stroke-width="4"/><path d="M88 56h22M88 68h22M88 80h22" stroke="#fff" stroke-width="4"/><circle cx="66" cy="52" r="7" fill="#fff"/><rect x="58" y="64" width="16" height="34" fill="#fff"/></svg>
    <h3>Guidance</h3><p>Lorem ipsum dolor sit consectetur adipiscing elit, sed do eiusmod</p>
  </div>
  <div class="service" style="left:864px">
    <svg class="blob" viewBox="0 0 180 160"><path d="M20 14h140c12 0 18 12 12 26-18 44-48 90-74 112-6 5-12 5-18 0C54 130 24 86 8 40 3 26 8 14 20 14z" fill="#0b4a7d" stroke="#fff" stroke-width="5"/><circle cx="84" cy="62" r="13" fill="none" stroke="#fff" stroke-width="4"/><path d="M60 108c0-18 10-28 24-28s24 10 24 28z" fill="none" stroke="#fff" stroke-width="4"/><circle cx="114" cy="44" r="10" fill="#fff"/></svg>
    <h3>Financial Advisors</h3><p>Lorem ipsum dolor sit consectetur adipiscing elit, sed do eiusmod</p>
  </div>
</section>

<section class="about">
  <div class="abs about-photo" role="img" aria-label="Water droplet falling into calm blue water"></div>
  <h2 class="heading">About us</h2>
  <p>Brookvale Advisors LLC is a consulting and recruiting firm that provides education, perspective, guidance, and assistance to financial advisors. Specifically, we are focused on serving two distinct profiles of client : First, we assist financial advisors as they explore, plan, and execute their professional journey to independence. Most typically , this transition involves leaving the advisor's existing broker/dealer and either joining a new broker/dealer as an independent</p>
  <div class="btn">Learn More <span class="dot"></span></div>
</section>

<section class="why">
  <h2 class="heading">Why choose us</h2>
  <div class="reason" style="left:107px;background:linear-gradient(180deg,#6e9cc8,#c9d6e0 45%,#4f6f8d)" role="img" aria-label="White motor yacht on the open sea"><span>Why work with me</span></div>
  <div class="reason" style="left:357px;background:linear-gradient(180deg,#9fa6a8,#c7cdcf 50%,#7d8588)" role="img" aria-label="Water droplet splashing on a still surface"><span>A fiduciary relationship</span></div>
  <div class="reason" style="left:607px;background:linear-gradient(180deg,#aab6be,#7d8a80 45%,#5e5a44)" role="img" aria-label="Hand holding a compass over green hills"><span>Services for teams</span></div>
  <div class="reason" style="left:857px;background:linear-gradient(180deg,#b9c4cc,#6c7b7e 45%,#4f5c66)" role="img" aria-label="Boats moored in a marina below hills"><span>Services for existing RIAs</span></div>
</section>

<section class="founder">
  <h2 class="heading">Dennis Halloway</h2>
  <p>Brookvale Advisors LLC is a consulting and recruiting firm that provides education, perspective, guidance, and assistance to financial advisors. Specifically,</p>
  <div class="contact-row" style="left:108px;top:239px;font-weight:500">
    <span class="ico"><svg width="16" height="16" viewBox="0 0 24 24"><path d="M6.6 10.8a15 15 0 0 0 6.6 6.6l2.2-2.2c.3-.3.7-.4 1-.2 1.1.4 2.3.6 3.6.6.6 0 1 .4 1 1V20c0 .6-.4 1-1 1A17 17 0 0 1 3 4c0-.6.4-1 1-1h3.5c.6 0 1 .4 1 1 0 1.3.2 2.5.6 3.6.1.3 0 .7-.2 1z" fill="#fff"/></svg></span>555-214-0387
  </div>
  <div class="contact-row" style="left:297px;top:239px;font-size:13.5px">
    <span class="ico"><svg width="16" height="14" viewBox="0 0 16 14"><rect x="1" y="2" width="14" height="10" rx="1" fill="none" stroke="#fff" stroke-width="2"/><path d="M1 3l7 5 7-5" fill="none" stroke="#fff" stroke-width="2"/></svg></span>dennis@brookvaleadvisors.com
  </div>
  <div class="contact-row" style="left:108px;top:291px;font-size:13.5px">
    <span class="ico"><svg width="14" height="14" viewBox="0 0 14 14"><circle cx="7" cy="7" r="4" fill="#fff"/></svg></span>https://www.brookvaleadvisors.com/team/dennis-halloway/
  </div>
  <div class="btn grey" style="left:110px;top:358px;width:158px;height:44px">Learn More <span class="dot"></span></div>
  <div class="abs frame"></div>
  <div class="abs portrait" role="img" aria-label="Portrait of the founder in a suit and light blue shirt"></div>
</section>

<section class="resources">
  <h2 class="heading">Resources</h2>
  <div class="round-arrow" style="left:28px"><svg width="12" height="18" viewBox="0 0 12 18"><path d="M9 2 2 9l7 7" fill="none" stroke="#111" stroke-width="2.5"/></svg></div>
  <div class="round-arrow" style="left:1122px"><svg width="12" height="18" viewBox="0 0 12 18"><path d="M3 2l7 7-7 7" fill="none" stroke="#111" stroke-width="2.5"/></svg></div>

  <article class="post" style="left:110px">
    <div class="pic" style="background:linear-gradient(180deg,#5f86bf,#bfd0e6 45%,#4d6f9b 75%,#6d8a3a)" role="img" aria-label="White yachts docked in a harbour"></div>
    <h4>Lorem ipsum dolor sit amet, con sectetur adipiscing</h4>
    <p>Sed ut perspiciatis unde omnis iste natus error sit voluptatem accusantium</p>
    <span class="more">Read more &raquo;</span>
    <div class="meta"><span>&#9638; 02 Nov 2020</span><span>&#9711; Laura Penfield</span></div>
  </article>
  <article class="post" style="left:438px">
    <div class="pic" style="background:radial-gradient(circle at 50% 50%,#e0c38f,#c9a468 60%,#a4804a)" role="img" aria-label="Antique parchment map"></div>
    <h4>Lorem ipsum dolor sit amet, con sectetur adipiscing</h4>
    <p>Sed ut perspiciatis unde omnis iste natus error sit voluptatem accusantium</p>
    <span class="more">Read more &raquo;</span>
    <div class="meta"><span>&#9638; 02 Nov 2020</span><span>&#9711; Laura Penfield</span></div>
  </article>
  <article class="post" style="left:767px">
    <div class="pic" style="background:linear-gradient(180deg,#bcc3c8,#9ca5ac 45%,#6f777c)" role="img" aria-label="Person sitting on a pier beside a marina"></div>
    <h4>Lorem ipsum dolor sit amet, con sectetur adipiscing</h4>
    <p>Sed ut perspiciatis unde omnis iste natus error sit voluptatem accusantium</p>
    <span class="more">Read more &raquo;</span>
    <div class="meta"><span>&#9638; 02 Nov 2020</span><span>&#9711; Laura Penfield</span></div>
  </article>
</section>

<section class="touch" role="img" aria-label="Blue-tinted waterfront with palm trees behind the contact form">
  <h2 class="heading" style="left:112px">Get in touch</h2>
  <div class="field" style="left:111px;top:121px;width:274px;height:46px">First Name</div>
  <div class="field" style="left:399px;top:121px;width:274px;height:46px">Last Name</div>
  <div class="field" style="left:111px;top:179px;width:274px;height:46px">Email</div>
  <div class="field" style="left:399px;top:179px;width:274px;height:46px">Phone No</div>
  <div class="field" style="left:111px;top:236px;width:562px;height:78px">Message</div>
  <div class="btn submit">Submit Now <span class="dot"></span></div>

  <h2 class="heading" style="left:782px">Contact us</h2>
  <div class="citem" style="top:128px"><span class="ico"><svg width="16" height="20" viewBox="0 0 16 20"><path d="M8 1a7 7 0 0 0-7 7c0 5 7 11 7 11s7-6 7-11a7 7 0 0 0-7-7z" fill="none" stroke="#0b4a7d" stroke-width="2"/><circle cx="8" cy="8" r="2.5" fill="#0b4a7d"/></svg></span>48 Harbor Lane, Easton Bay<br>United States</div>
  <div class="citem" style="top:201px"><span class="ico"><svg width="18" height="18" viewBox="0 0 24 24"><path d="M6.6 10.8a15 15 0 0 0 6.6 6.6l2.2-2.2c.3-.3.7-.4 1-.2 1.1.4 2.3.6 3.6.6.6 0 1 .4 1 1V20c0 .6-.4 1-1 1A17 17 0 0 1 3 4c0-.6.4-1 1-1h3.5c.6 0 1 .4 1 1 0 1.3.2 2.5.6 3.6.1.3 0 .7-.2 1z" fill="#0b4a7d"/></svg></span>1 800 555 0142</div>
  <div class="citem" style="top:272px"><span class="ico"><svg width="18" height="14" viewBox="0 0 16 14"><rect x="1" y="2" width="14" height="10" rx="1" fill="none" stroke="#0b4a7d" stroke-width="2"/><path d="M1 3l7 5 7-5" fill="none" stroke="#0b4a7d" stroke-width="2"/></svg></span>info@brookvaleadvisors.com</div>
</section>

<footer class="site-footer">
  <nav class="foot-nav"><span>Home</span><span>About</span><span>Services Offered</span><span>Contact</span><span>Resources</span></nav>
  <div class="social"><i></i><i></i><i style="background:#d9473b"></i><i style="background:#1b6fb5"></i></div>
  <p class="copy">&copy; 2021 Brookvale Advisors. All Rights Reserved</p>
</footer>

</body>
</html>
```